Flyer Design Project

Training and Consulting Flyer

I attached a document that contained the wording for the flyer as well as the logo.

Target Market(s)

Little Compass agencies and grantees

Industry/Entity Type

Training

Font styles to use
Sans Serif

Colors
e667a6
eda3c7
a54499
b768aa
f9d9e8

Requirements
Must have
• Words provided on attachment
Nice to have
• Graphics that are related to adult training/learning and consulting

```html
<!DOCTYPE html>
<html lang="en">
<head>
<meta charset="utf-8">
<title>Rowan Bay Health – Training and Consulting Flyer</title>
<link href="https://fonts.googleapis.com/css2?family=Open+Sans:wght@300;400;600;700&display=swap" rel="stylesheet">
<style>
  :root {
    --page-bg: #e9e7e8;
    --paper: #ffffff;
    --blush: #f6b9c0;
    --plum: #5c2a4f;
    --berry: #a0447f;
    --rose: #c4698b;
    --card: #c7728f;
    --card-num: #b8647f;
    --grey: #5f5f63;
    --footer-stripe: #c7728f;
    --gold: #f3c21c;
    --white: #ffffff;
  }
  * { margin: 0; padding: 0; box-sizing: border-box; }
  html, body { width: 1200px; height: 2250px; overflow: hidden; }
  body {
    background: var(--page-bg);
    font-family: "Open Sans", Arial, sans-serif;
    position: relative;
  }
  .flyer {
    position: absolute;
    left: 50px; top: 414px;
    width: 1100px; height: 1422px;
    background: linear-gradient(215deg, var(--blush) 0%, #fbe1e4 30%, var(--paper) 58%);
    box-shadow: 0 10px 30px rgba(0,0,0,.18);
    overflow: hidden;
  }
  .decor-butterflies {
    position: absolute;
    left: 680px; top: 50px;
    width: 380px; height: 440px;
    border-radius: 50%;
    background: radial-gradient(ellipse at center, rgba(236,160,182,.45) 0%, rgba(246,185,192,0) 70%);
  }
  .brand {
    position: absolute;
    left: 142px; top: 150px;
    display: flex; align-items: center; gap: 14px;
  }
  .brand-dot { width: 30px; height: 30px; border-radius: 50%; background: var(--berry); }
  .brand-name {
    font-weight: 700; font-size: 30px; line-height: 1;
    color: var(--plum); letter-spacing: .3px;
  }
  .headline {
    position: absolute; left: 143px; top: 290px;
    font-size: 54px; font-weight: 400; letter-spacing: -.5px; line-height: 1;
  }
  .headline .w1 { color: var(--plum); }
  .headline .w2 { color: var(--berry); }
  .headline .w3 { color: var(--grey); }
  .company {
    position: absolute; left: 140px; top: 368px;
    color: var(--rose); line-height: .98;
  }
  .company-main { font-size: 84px; font-weight: 700; letter-spacing: -1.5px; display: block; }
  .company-sub { font-size: 84px; font-weight: 300; display: block; }
  .lede {
    position: absolute; left: 143px; top: 568px; width: 815px;
    font-size: 18.5px; font-weight: 700; color: var(--grey); line-height: 1.3;
    letter-spacing: -.2px;
  }
  .intro {
    position: absolute; left: 143px; top: 638px; width: 815px;
    font-size: 18.5px; font-weight: 700; color: var(--berry); line-height: 1.3;
    letter-spacing: -.2px; text-align: justify;
  }
  .service {
    position: absolute; width: 376px; height: 190px;
    background: var(--card);
    border-radius: 6px 6px 22px 6px;
    box-shadow: 6px 8px 14px rgba(0,0,0,.18);
    overflow: hidden;
  }
  .service-num {
    position: absolute; left: 14px; top: -18px;
    font-size: 220px; font-weight: 700; color: var(--card-num); line-height: 1;
  }
  .service-text {
    position: relative; padding: 22px 24px 0 26px;
    color: var(--white); font-size: 17.5px; line-height: 1.38; text-align: justify;
  }
  .s1 { left: 147px; top: 751px; }
  .s2 { left: 577px; top: 754px; }
  .s3 { left: 147px; top: 988px; }
  .s4 { left: 577px; top: 988px; }
  .s1 .service-text, .s3 .service-text { padding-top: 34px; }
  .signature {
    position: absolute; left: 0; right: 0; top: 1236px;
    text-align: center; font-size: 25px; color: var(--plum);
  }
  .signature small { font-size: 15px; }
  .footer-stripe {
    position: absolute; left: 0; right: 0; top: 1307px; height: 10px;
    background: var(--footer-stripe);
  }
  .footer {
    position: absolute; left: 0; right: 0; top: 1317px; bottom: 0;
    background: var(--plum);
    display: flex; align-items: center; justify-content: center; gap: 40px;
    color: var(--white); font-size: 21px;
  }
  .contact { display: flex; align-items: center; gap: 12px; white-space: nowrap; }
  .contact svg { width: 18px; height: 18px; fill: var(--gold); }
</style>
</head>
<body>
  <main class="flyer">
    <div class="decor-butterflies" role="img" aria-label="Soft pink butterfly line illustrations"></div>

    <div class="brand">
      <span class="brand-dot"></span>
      <span class="brand-name">Rowan Bay Health</span>
    </div>

    <h1 class="headline"><span class="w1">Planning</span> <span class="w2">Training</span> <span class="w3">Results</span></h1>
    <h2 class="company"><span class="company-main">Health Consultants</span><span class="company-sub">&amp; Group</span></h2>

    <p class="lede">Innovative Approaches to meeting the 5 year funding measures in the content area of health, Nutrition, Oral Health &amp; Safety</p>
    <p class="intro">Rowan Bay Health consultants has embarked on a new methodology deigned ensure programs meet total requirements as prescribed under the health Services program.</p>

    <section class="service s1">
      <span class="service-num">1</span>
      <p class="service-text">Let us manage your health tips program through remote and offsite measures to ensure total compliance and strategic methodology toward quality service approaches.</p>
    </section>
    <section class="service s2">
      <span class="service-num">2</span>
      <p class="service-text">Let us provide consultants to mentor your health manager nutrition content specialist facilities safety manager these support consultant are advanced level academies in their specialized areas of focus.</p>
    </section>
    <section class="service s3">
      <span class="service-num">3</span>
      <p class="service-text">Let us provide advanced based Mock Reviews for your program designed to assist management staff in focus I, Focus II Review strategies for 2018.</p>
    </section>
    <section class="service s4">
      <span class="service-num">4</span>
      <p class="service-text">Let us provide T / TA for any new Health, Nutritionand Safety staff to ensure they are fully prepared to perform their job duties at their highest level of management approaches.</p>
    </section>

    <p class="signature">Dana Morrell <small>CEO</small></p>

    <div class="footer-stripe"></div>
    <footer class="footer">
      <span class="contact">
        <svg viewBox="0 0 24 24" aria-hidden="true"><path d="M12 1a8 8 0 0 0-8 8c0 6 8 14 8 14s8-8 8-14a8 8 0 0 0-8-8zm0 11a3 3 0 1 1 0-6 3 3 0 0 1 0 6z"/></svg>
        P.O. Box 4821 Brookhaven, GA 30319
      </span>
      <span class="contact">
        <svg viewBox="0 0 24 24" aria-hidden="true"><path d="M6.6 10.8a15 15 0 0 0 6.6 6.6l2.2-2.2a1 1 0 0 1 1-.25 11.4 11.4 0 0 0 3.6.57 1 1 0 0 1 1 1V20a1 1 0 0 1-1 1A17 17 0 0 1 3 4a1 1 0 0 1 1-1h3.5a1 1 0 0 1 1 1c0 1.25.2 2.45.57 3.57a1 1 0 0 1-.25 1z"/></svg>
        (555) 014-2867
      </span>
      <span class="contact">
        <svg viewBox="0 0 24 24" aria-hidden="true"><path d="M2 5h20v14H2z M2 5l10 8 10-8" stroke="#5c2a4f" stroke-width="1.5"/></svg>
        hello@rowanbay.example
      </span>
    </footer>
  </main>
</body>
</html>
```